Harborlane Consultants LLC web site

Harborlane Consultants LLC is a consulting and recruiting firm that provides education, perspective, guidance, and assistance to financial advisors. Dennis Malbrook is the founder of this new firm and is the only employee at this time.
Please see the attached overview which will provide much narrative describing the firm, its purpose, scope of services offered, and other useful information to help you design a web site.

Target Market(s)

US based financial advisors who are looking to transition their business to an independent ( non-employee ) business model.

Industry/Entity Type

Consultant

Coding

Coded - Design and coding required

Number of Pages Required

5+ page

Font styles to use
Sans Serif

Requirements
Must have
• all relevant pages for a basic web site : Home, About, Services offered, Contact, Resources , etc.
Nice to have
• color scheme : see logo in the attached briefing document

```html
<!DOCTYPE html>
<html lang="en">
<head>
<meta charset="utf-8">
<title>Harborlane Consultants LLC</title>
<link href="https://fonts.googleapis.com/css2?family=Montserrat:wght@300;400;500;600;700;800&family=Open+Sans:wght@400;600&display=swap" rel="stylesheet">
<style>
:root{
  --navy-deep:#0c2842;
  --navy:#084a80;
  --blue-bright:#2a83f7;
  --yellow:#fff200;
  --ink:#111318;
  --body:#4a4d55;
  --grey-band:#f4f4f4;
  --foot:#f1f2f4;
  --white:#ffffff;
}
*{margin:0;padding:0;box-sizing:border-box}
html,body{width:1200px;height:2741px;overflow:hidden}
body{position:relative;font-family:"Open Sans",sans-serif;color:var(--body);background:var(--white)}
.abs{position:absolute}
.head{font-family:"Montserrat",sans-serif}
.btn{position:absolute;display:flex;align-items:center;justify-content:center;font-family:"Montserrat",sans-serif;font-weight:700;font-size:13px;letter-spacing:.5px;color:var(--white);background:var(--navy);text-transform:uppercase;border-radius:2px}

/* hero */
.hero{position:absolute;left:0;top:0;width:1200px;height:574px;background:linear-gradient(90deg,#0d2c48,#0c2a44 60%,#0e2f4f);overflow:hidden}
.hero-blob{position:absolute;left:0;top:0}
.founder-photo{position:absolute;left:510px;top:55px;width:565px;height:519px;border-radius:230px 230px 0 0;background:linear-gradient(180deg,#d9a88c 0%,#c99379 35%,#e9eef6 55%,#1c2a44 75%,#18253d 100%)}
.brand{position:absolute;left:168px;top:22px;display:flex;align-items:center;gap:9px;font-family:"Montserrat",sans-serif;font-weight:600;color:var(--white);font-size:17px;letter-spacing:1.5px}
.brand .dot{width:34px;height:34px;border-radius:50%;background:var(--white)}
.nav{position:absolute;top:28px;left:491px;display:flex;gap:0;font-family:"Montserrat",sans-serif;font-weight:500;font-size:12.5px;color:var(--white)}
.nav span{position:absolute;white-space:nowrap}
.hero-title{position:absolute;left:182px;top:160px;color:var(--white);font-family:"Montserrat",sans-serif}
.hero-title .big{font-size:64px;font-weight:800;line-height:66px;letter-spacing:-1px}
.hero-title .light{font-size:46px;font-weight:300;line-height:50px}
.hero-sub{position:absolute;left:182px;top:280px;width:380px;font-family:"Montserrat",sans-serif;font-weight:400;font-size:18.5px;line-height:22px;color:var(--white)}
.sig{position:absolute;left:414px;top:338px;font-family:"Montserrat",sans-serif;font-weight:600;font-size:19px;color:var(--yellow)}
.sig-role{position:absolute;left:414px;top:366px;font-family:"Montserrat",sans-serif;font-size:12px;color:var(--white)}
.btn-yellow{background:var(--yellow);color:var(--ink)}

/* about */
.photo{position:absolute}
.about h2,.why h2{font-family:"Montserrat",sans-serif;font-weight:800;font-size:36px;color:var(--ink);letter-spacing:.5px}
.para{font-size:12px;line-height:15px;color:var(--body)}
.para p+p{margin-top:15px}

/* why */
.why{position:absolute;left:0;top:1205px;width:1200px;height:525px;background:var(--grey-band)}
.why h2 .accent{color:var(--navy)}

/* services */
.services-title{position:absolute;left:0;width:1200px;top:1790px;text-align:center;font-family:"Montserrat",sans-serif;font-weight:600;font-size:27px;color:var(--ink)}
.services-intro{position:absolute;left:300px;width:600px;top:1842px;text-align:center;font-size:12px;line-height:16.5px}
.card{position:absolute;top:1916px;height:127px;border:1px solid #e3e4e7;background:var(--white);padding:14px 5px 0 5px}
.card h3{font-family:"Montserrat",sans-serif;font-weight:700;font-size:13.5px;line-height:16px;color:var(--ink);padding-right:40px}
.card .mark{position:absolute;right:32px;top:14px;width:32px;height:32px;border-radius:50%;border:3px solid var(--navy)}
.card ul{list-style:none;margin-top:12px;font-size:8.5px;line-height:11.5px;color:var(--body)}
.card ul li::before{content:"• "}
.pager{position:absolute;top:2097px;width:10px;height:10px;border-radius:50%}

/* cta */
.cta{position:absolute;left:0;top:2163px;width:1200px;height:343px;background:linear-gradient(90deg,#f3f5f8 0%,#eef1f5 45%,#d9dee6 70%,#e6e9ee 100%)}
.cta-title{position:absolute;left:0;width:1200px;top:2245px;text-align:center;font-family:"Montserrat",sans-serif;font-weight:800;font-size:36px;line-height:44px;color:var(--navy)}
.cta-sub{position:absolute;left:0;width:1200px;top:2336px;text-align:center;font-family:"Montserrat",sans-serif;font-weight:400;font-size:17px;line-height:21px;color:#555a63}

/* footer */
.footer{position:absolute;left:0;top:2506px;width:1200px;height:235px;background:var(--foot)}
.foot-brand{position:absolute;left:170px;top:2556px;display:flex;align-items:center;gap:10px;font-family:"Montserrat",sans-serif;font-weight:600;font-size:20px;letter-spacing:1.5px;color:var(--navy)}
.foot-brand .dot{width:46px;height:46px;border-radius:50%;background:var(--navy)}
.foot-text{position:absolute;left:170px;top:2617px;width:232px;font-size:11px;line-height:14px;color:#555}
.foot-col{position:absolute;top:2541px}
.foot-col h4{font-family:"Montserrat",sans-serif;font-weight:700;font-size:18.5px;color:var(--navy);margin-bottom:13px}
.foot-col a{display:block;font-size:10.5px;line-height:21px;color:#555;text-decoration:none}
.foot-col .strong{color:var(--navy);font-weight:600}
.copy{position:absolute;left:170px;top:2703px;font-size:10px;color:#555}
.social{position:absolute;top:2703px;width:14px;height:14px;border-radius:50%;background:var(--navy)}
</style>
</head>
<body>

<header class="hero">
  <div class="founder-photo" role="img" aria-label="Portrait of founder in navy blazer and striped shirt"></div>
  <svg class="hero-blob" width="1200" height="574" viewBox="0 0 1200 574" aria-hidden="true">
    <path d="M1200 30 C1120 25 1085 90 1065 130 C1040 175 955 150 890 185 C835 215 835 285 885 345 C935 405 1010 460 1075 574 L1200 574 Z" fill="#2a83f7"/>
  </svg>
  <div class="brand"><span class="dot"></span>HARBORLANE</div>
  <nav class="nav">
    <span style="left:0">HOME</span>
    <span style="left:60px">ABOUT</span>
    <span style="left:122px">SERVICES OFFERED</span>
    <span style="left:260px">CONTACT</span>
    <span style="left:338px">RESOURCES</span>
  </nav>
  <a class="btn" style="left:931px;top:20px;width:100px;height:28px;font-size:11px;">Get Started</a>
  <div class="hero-title"><div class="big">Harborlane</div><div class="light">Consultants LLC</div></div>
  <div class="hero-sub">helping financial advisors to navigate their journey to independence</div>
  <div class="sig">Dennis Malbrook</div>
  <div class="sig-role">Founder</div>
  <a class="btn btn-yellow" style="left:182px;top:371px;width:137px;height:34px;">Contact Us</a>
</header>

<section class="about">
  <div class="photo" style="left:174px;top:665px;width:376px;height:368px;background:linear-gradient(135deg,#cfd4da,#8a97a8 50%,#2c3a52)" role="img" aria-label="Two colleagues reviewing documents in an office"></div>
  <div class="photo" style="left:284px;top:889px;width:322px;height:247px;background:#fff"></div>
  <div class="photo" style="left:294px;top:901px;width:300px;height:225px;background:linear-gradient(135deg,#e8e9ea,#b9b3a8 50%,#6d6a66)" role="img" aria-label="Advisor meeting with clients at a desk"></div>
  <h2 class="abs" style="left:663px;top:702px;">ABOUT</h2>
  <div class="abs para" style="left:663px;top:755px;width:340px;">
    <p>Harborlane Consultants LLC is a consulting and recruiting firm that provides education, perspective, guidance, and assistance to financial advisors. Specifically, we are focused on serving two distinct profiles of client</p>
    <p>First, we assist financial advisors as they explore, plan, and execute their professional journey to independence. Most typically , this transition involves leaving the advisor’s existing broker/dealer and either joining a new broker/dealer as an independent rep or establishing and launching a new and independent firm as a Registered Investment Advisor , or RIA.</p>
  </div>
  <a class="btn" style="left:661px;top:946px;width:128px;height:34px;">Learn More</a>
</section>

<section class="why">
  <h2 class="abs" style="left:170px;top:107px;">WHY WORK <span class="accent">WITH ME ?</span></h2>
  <div class="abs para" style="left:170px;top:160px;width:418px;">
    <p>In short, experience. I have spent my entire 35 year career in this industry, with the last 22 years spent in this exact endeavor... helping advisors like you to learn about, envision , and realize their dream of becoming independent advisors and business owners.</p>
    <p>My range of experience includes roles within many of the top companies in the financial services industry and includes positions in trading, institutional sales, retirement plan consulting, retail advisory, RIA custody sales, IBD regional management, executive director for business development (for a large strategic intermediary firm), and head of breakaway strategy for a large RIA custody provider.</p>
  </div>
  <a class="btn" style="left:170px;top:361px;width:128px;height:34px;">Learn More</a>
  <svg class="abs" style="left:620px;top:45px" width="450" height="425" viewBox="0 0 450 425">
    <path d="M130 20 C250 0 400 10 440 120 C470 210 380 330 300 395 C240 440 170 430 130 380 C90 320 20 250 10 170 C0 90 40 35 130 20 Z" fill="#084a80"/>
    <path d="M115 30 C230 15 355 30 385 125 C410 210 340 320 270 385 C220 430 160 420 125 375 C90 320 25 250 15 170 C5 95 40 45 115 30 Z" fill="#b8bcc2" role="img" aria-label="Business team joining fists together"/>
  </svg>
</section>

<section class="services">
  <h2 class="services-title">Services for existing RIAs</h2>
  <p class="services-intro">Let’s face it. You have a business to run. You have clients , and you have assets, both of which give you plenty to worry about. You have organic growth goals and are busy trying to achieve them. You may also have an interest in inorganic growth, whether that be from acquisitions or recruiting.</p>
  <div class="card" style="left:168px;width:225px;"><span class="mark"></span><h3>Inorganic growth consulting program</h3><ul><li>guided process for successful advisor recruiting</li><li>prospect pipeline - development and management</li><li>acquisitions targeting</li></ul></div>
  <div class="card" style="left:400px;width:216px;"><span class="mark"></span><h3>RIA deep discovery and profiling</h3><ul><li>articulation of value proposition for advisors</li><li>advise on offering for advisors ... the "winning formula" to attract FAs , teams, RIAs</li></ul></div>
  <div class="card" style="left:623px;width:202px;"><span class="mark"></span><h3>Validation of current service providers</h3><ul><li>advise on alternative solutions based upon needs of firm</li></ul></div>
  <div class="card" style="left:831px;width:201px;"><span class="mark"></span><h3>Optimize pricing &amp; profitability for advisor recruits</h3><ul><li>pro-forma economic analysis for firm and for recruit ( custom lens for each )</li></ul></div>
  <span class="pager" style="left:586px;background:var(--navy)"></span>
  <span class="pager" style="left:603px;border:1px solid #777"></span>
</section>

<section class="cta" role="img" aria-label="Soft faded photo of a businessman on a phone call"></section>
<h2 class="cta-title">ARE YOU READY TO<br>“WORK WITH HARBORLANE” ?</h2>
<p class="cta-sub">schedule a confidential ( and free ) exploratory meeting with me , and<br>let’s see if we can work together.</p>
<a class="btn" style="left:517px;top:2404px;width:166px;height:34px;">Get Started Now</a>

<footer class="footer"></footer>
<div class="foot-brand"><span class="dot"></span>HARBORLANE</div>
<p class="foot-text">Lorem ipsum dolor sit amet, consectetur adipiscing elit, sed do eiusmod tempor incid-idunt ut labore et dolore magna aliqua.</p>
<div class="foot-col" style="left:471px"><h4>Explore</h4><a>Success Stories</a><a>About Us</a><a>Sitemap</a><a>Press</a><a>Events</a></div>
<div class="foot-col" style="left:651px"><h4>Contact</h4><a class="strong">Schedule an exploratory meeting now</a><a>Dennis Malbrook</a><a>555-218-7730</a><a>dennis@harborlane-advisory.com</a></div>
<div class="foot-col" style="left:921px"><h4>Help</h4><a>Contact Us</a><a>FAQS</a><a>Cookie Policy</a></div>
<p class="copy">© 2021. Harborlane Consultants All Rights Reserved.</p>
<span class="social" style="left:903px"></span>
<span class="social" style="left:928px"></span>
<span class="social" style="left:956px"></span>
<span class="social" style="left:984px"></span>
<span class="social" style="left:1014px"></span>
</body>
</html>
```